Business Card Design for a Personal Trainer

I need a business card design for my job as a personal trainer. It should have a unique, modern and exclusive design. On the front there should be only my logo with my name and my job. 0163/2918374 Tobias Kellinger Lindenfeldweg 14 80412 Munich Germany The most important contact information is the web adress. it can be bigger than the rest, but its not necessary. The card should be 8,5cmx5,5cm big. Font: Roboto. Colors: black, white, gray, 56c1ff.

```html
<!DOCTYPE html>
<html lang="de">
<head>
<meta charset="utf-8">
<title>Tobias Kellinger – Business Cards</title>
<link href="https://fonts.googleapis.com/css2?family=Roboto:wght@300;400;500;700;900&display=swap" rel="stylesheet">
<style>
  :root {
    --sky: #56c1ff;
    --sky-deep: #45b3f5;
    --white: #ffffff;
    --gray: #7a7a7a;
    --ink: #111111;
    --backdrop: #5e5e5e;
  }
  html, body {
    margin: 0;
    width: 1200px;
    height: 1200px;
    overflow: hidden;
    background: var(--backdrop);
    font-family: "Roboto", Arial, sans-serif;
  }
  .stage { position: relative; width: 1200px; height: 1200px; }
  .card {
    position: absolute;
    left: 190px;
    width: 820px;
    height: 531px;
    overflow: hidden;
    box-shadow: 0 10px 30px rgba(0,0,0,0.35);
  }
  .card--front { top: 46px; background: linear-gradient(160deg, var(--sky-deep), var(--sky)); }
  .card--back { top: 623px; background: var(--sky); }

  /* Front */
  .front-frame { position: absolute; inset: 0; }
  .brand {
    position: absolute;
    left: 0; right: 0; top: 190px;
    display: flex;
    align-items: center;
    justify-content: center;
    gap: 26px;
  }
  .brand__text { display: flex; flex-direction: column; align-items: stretch; }
  .brand__name {
    color: var(--white);
    font-weight: 400;
    font-size: 50px;
    line-height: 1;
    letter-spacing: 3px;
    text-transform: uppercase;
  }
  .brand__role {
    display: flex;
    align-items: center;
    gap: 12px;
    margin-top: 12px;
    color: var(--white);
    font-weight: 300;
    font-size: 18px;
    letter-spacing: 9px;
    text-transform: uppercase;
  }
  .brand__role::before, .brand__role::after {
    content: "";
    flex: 1;
    height: 2px;
    background: var(--white);
  }
  .brand__mark { width: 72px; height: 72px; background: var(--white); }
  .front-web {
    position: absolute;
    left: 130px;
    bottom: 22px;
    margin: 0;
    padding: 0 10px;
    color: var(--ink);
    font-weight: 700;
    font-size: 30px;
    line-height: 1;
  }

  /* Back */
  .back-art { position: absolute; inset: 0; }
  .contact { position: absolute; left: 42px; top: 36px; color: var(--white); }
  .contact__name { margin: 0 0 22px; font-weight: 900; font-size: 50px; line-height: 1; }
  .contact__name .surname { color: var(--gray); }
  .contact__address { margin: 0 0 34px; font-weight: 700; font-size: 20px; line-height: 1.25; }
  .contact__line {
    display: flex;
    align-items: center;
    gap: 10px;
    margin: 0 0 8px;
    font-weight: 500;
    font-size: 19px;
  }
  .contact__icon { width: 26px; height: 26px; flex: none; }
  .contact__web {
    position: absolute;
    left: 42px;
    bottom: 40px;
    margin: 0;
    color: var(--white);
    font-weight: 900;
    font-size: 31px;
    line-height: 1;
  }
  .contact__web .domain { color: var(--gray); }
</style>
</head>
<body>
<main class="stage">

  <section class="card card--front" aria-label="Card front">
    <svg class="front-frame" width="820" height="531" viewBox="0 0 820 531">
      <path d="M120 493 H36 V38 H784 V493 H470" fill="none" stroke="#ffffff" stroke-width="3"/>
    </svg>
    <div class="brand">
      <div class="brand__text">
        <span class="brand__name">Tobias Kellinger</span>
        <span class="brand__role">Personal Trainer</span>
      </div>
      <span class="brand__mark"></span>
    </div>
    <p class="front-web">www.tobiaskellinger.de</p>
  </section>

  <section class="card card--back" aria-label="Card back">
    <svg class="back-art" width="820" height="531" viewBox="0 0 820 531">
      <defs>
        <linearGradient id="portraitTone" x1="0" y1="0" x2="1" y2="1">
          <stop offset="0" stop-color="#f4f4f4"/>
          <stop offset="0.55" stop-color="#6d6d6d"/>
          <stop offset="1" stop-color="#2b2b2b"/>
        </linearGradient>
      </defs>
      <path d="M680 0 Q480 230 520 531" fill="none" stroke="#8c8c8c" stroke-width="30"/>
      <path d="M697 0 Q497 232 537 531" fill="none" stroke="#2a2a2a" stroke-width="3"/>
      <path d="M704 0 Q504 233 544 531 L820 531 L820 0 Z" fill="url(#portraitTone)"
            role="img" aria-label="Black and white portrait of the trainer, arms crossed, in a fitted long-sleeve shirt"/>
    </svg>

    <div class="contact">
      <h1 class="contact__name">Tobias <span class="surname">Kellinger</span></h1>
      <p class="contact__address">Lindenfeldweg 14<br>80412 München</p>
      <p class="contact__line">
        <svg class="contact__icon" viewBox="0 0 26 26" aria-hidden="true">
          <circle cx="13" cy="13" r="11.5" fill="none" stroke="#fff" stroke-width="2"/>
          <path d="M9 7.5 L11 7 L12.3 10 L10.9 11.2 Q12 13.8 14.8 15.1 L16 13.7 L19 15 L18.5 17 Q17.5 18.5 15 17.8 Q9.5 15.8 8 10.5 Q7.6 8.3 9 7.5 Z" fill="#fff"/>
        </svg>
        0163/2918374
      </p>
      <p class="contact__line">
        <svg class="contact__icon" viewBox="0 0 26 26" aria-hidden="true">
          <circle cx="13" cy="13" r="11.5" fill="none" stroke="#fff" stroke-width="2"/>
          <rect x="7" y="8.5" width="12" height="9" rx="1" fill="#fff"/>
          <path d="M7.5 9 L13 13.5 L18.5 9" fill="none" stroke="#56c1ff" stroke-width="1.5"/>
        </svg>
        t.kellinger@postfach-mail.de
      </p>
    </div>
    <p class="contact__web">www.<span class="domain">tobiaskellinger</span>.de</p>
  </section>

</main>
</body>
</html>
```